Student Business Card Design

As you already know, I'm a student at BV majoring in Supply Chain & Logistics Technology. I want a business card design that leaves the recipient impressed. A clean, professional, and memorable design is desired without too much color. My school's logo can be found online. I'd like to have that on the card.

Target Market(s)

Anyone who is a recruiter or an employer who has authority to hire.

Industry/Entity Type

Business

Contact Information for Business Card

Name: Osman Velibor

Phone Number: 614-275-3316

Email Address: velibor.osman@mailbox-demo.net

Major: Supply Chain & Logistics Technology

Minor: Purchasing

University: Marlowe State University

College: Ashcombe School of Engineering

I want a Workvine logo with my name beside it.

Also, on the back of the card I want this quote: "If it doesn't challenge you, it doesn't change you"-, Lena Sorbach

Requirements
Must have
• I'd like to see a Workvine logo go with my name.
• Professional-I'm going to be handing this card out in career fairs and networking events.
Nice to have
• Marlowe State University's colors: white, silver, and red, but if you feel it's better to go with a different color scheme then do it.
Should not have
• No white space on the design.

```html
<!DOCTYPE html>
<html lang="en">
<head>
<meta charset="utf-8">
<title>Osman Velibor – Business Card</title>
<link rel="stylesheet" href="https://fonts.googleapis.com/css2?family=Roboto+Condensed:wght@400;700&family=Alike&family=Fresca&display=swap">
<style>
  :root {
    --stage: #c8141c;
    --card: #f7f6f4;
    --ink: #1b1b1b;
    --red: #d8141c;
    --quote-red: #cc0f18;
    --social-blue: #5a9fd8;
  }
  * { margin: 0; padding: 0; box-sizing: border-box; }
  html, body { width: 1200px; height: 664px; overflow: hidden; }
  body { background: var(--stage); position: relative; }

  .card {
    position: absolute;
    top: 49px;
    width: 532px;
    height: 314px;
    border-radius: 26px;
    background: var(--card);
    overflow: hidden;
  }
  .card--front { left: 54px; }
  .card--back { left: 610px; }

  /* Front */
  .identity__name-row {
    position: absolute; left: 246px; top: 50px;
    display: flex; align-items: center; gap: 7px;
    white-space: nowrap;
  }
  .identity__name {
    font-family: "Roboto Condensed", sans-serif;
    font-weight: 700;
    font-size: 29px;
    letter-spacing: -0.4px;
    color: var(--red);
    text-transform: uppercase;
    line-height: 1;
  }
  .identity__divider { width: 1px; height: 20px; background: var(--ink); flex: none; }
  .identity__social {
    font-family: "Roboto Condensed", sans-serif;
    font-weight: 700;
    font-size: 14px;
    color: var(--social-blue);
    line-height: 1;
  }
  .identity__minor {
    position: absolute; left: 246px; top: 90px;
    font-family: "Roboto Condensed", sans-serif;
    font-weight: 700;
    font-size: 16px;
    color: var(--ink);
    text-transform: uppercase;
    line-height: 1.1;
    white-space: nowrap;
  }
  .identity__major {
    position: absolute; left: 246px; top: 109px;
    font-family: "Roboto Condensed", sans-serif;
    font-size: 16.5px;
    color: var(--ink);
    line-height: 1.2;
    white-space: nowrap;
  }

  .contact { position: absolute; left: 246px; top: 152px; list-style: none; }
  .contact__item {
    display: flex; align-items: center; gap: 10px;
    height: 26px;
    font-family: "Roboto Condensed", sans-serif;
    font-size: 16px;
    color: var(--ink);
    white-space: nowrap;
  }
  .contact__icon { width: 18px; height: 18px; flex: none; }

  .school { position: absolute; left: 246px; top: 220px; display: flex; align-items: center; gap: 8px; white-space: nowrap; }
  .school__mark {
    font-family: "Roboto Condensed", sans-serif;
    font-weight: 700;
    font-size: 32px;
    color: var(--red);
    line-height: 1;
  }
  .school__name {
    font-family: "Roboto Condensed", sans-serif;
    font-weight: 700;
    color: var(--ink);
    line-height: 1.15;
  }
  .school__university { font-size: 14px; text-transform: uppercase; display: block; }
  .school__college { font-size: 16px; display: block; }

  /* Back */
  .quote {
    position: absolute; left: 0; right: 0; top: 95px;
    font-family: "Alike", serif;
    font-size: 22px;
    color: var(--ink);
    white-space: nowrap;
  }
  .quote__line { display: block; line-height: 40px; }
  .quote__line--first { padding-left: 100px; }
  .quote__line--second { padding-left: 170px; }
  .quote__mark {
    font-size: 48px;
    color: var(--quote-red);
    line-height: 0;
    vertical-align: -10px;
  }
  .quote__accent { color: var(--quote-red); }
  .quote__author {
    position: absolute; left: 215px; top: 180px;
    font-family: "Fresca", sans-serif;
    font-size: 26px;
    color: var(--quote-red);
    white-space: nowrap;
  }
</style>
</head>
<body>
  <section class="card card--front" aria-label="Card front">
    <div class="identity__name-row">
      <h1 class="identity__name">Osman Velibor</h1>
      <span class="identity__divider"></span>
      <span class="identity__social">Workvine</span>
    </div>
    <p class="identity__minor">Purchasing</p>
    <p class="identity__major">Supply Chain &amp; Logistics Technology</p>

    <ul class="contact">
      <li class="contact__item">
        <svg class="contact__icon" viewBox="0 0 18 18" aria-hidden="true">
          <circle cx="9" cy="9" r="9" fill="#d8141c"/>
          <rect x="6" y="3.5" width="6" height="11" rx="1.2" fill="#fff"/>
          <rect x="7" y="5" width="4" height="7" fill="#d8141c"/>
        </svg>
        614-275-3316
      </li>
      <li class="contact__item">
        <svg class="contact__icon" viewBox="0 0 18 18" aria-hidden="true">
          <circle cx="9" cy="9" r="8" fill="none" stroke="#d8141c" stroke-width="1.6"/>
          <rect x="4.5" y="6" width="9" height="6.5" fill="none" stroke="#d8141c" stroke-width="1.3"/>
          <path d="M4.5 6 L9 10 L13.5 6 M4.5 12.5 L8 9.2 M13.5 12.5 L10 9.2" fill="none" stroke="#d8141c" stroke-width="1.2"/>
        </svg>
        velibor.osman@mailbox-demo.net
      </li>
    </ul>

    <div class="school">
      <span class="school__mark">BV</span>
      <span class="school__name">
        <span class="school__university">Marlowe State University</span>
        <span class="school__college">Ashcombe School of Engineering</span>
      </span>
    </div>
  </section>

  <section class="card card--back" aria-label="Card back">
    <blockquote class="quote">
      <span class="quote__line quote__line--first"><span class="quote__mark">&ldquo;</span>If it doesn't <span class="quote__accent">CHALLENGE</span> you,</span>
      <span class="quote__line quote__line--second">it doesn't <span class="quote__accent">CHANGE</span> you<span class="quote__mark">&rdquo;</span></span>
    </blockquote>
    <p class="quote__author">- Lena Sorbach</p>
  </section>
</body>
</html>
```